Oru Loft Business Card

We need a business card designed for a a company called "Oru Loft". We offer consulting, coaching and training to business leaders and coaches (across the world) using the latest findings in neuroscience, social and emotional intelligence and positive psychology. The final design should communicate the use of brain science to create sustainable relationships.

The card should be doublesided. The logo is attached and names and titles will be provided to the successful designer. Thank you.

```html
<!DOCTYPE html>
<html lang="en">
<head>
<meta charset="utf-8">
<title>Oru Loft Business Card</title>
<link rel="stylesheet" href="https://fonts.googleapis.com/css2?family=Open+Sans:wght@400;600;700&display=swap">
<style>
  :root {
    --backdrop: #3a3a3c;
    --brand-blue: #0089bf;
    --deep-blue: #006b9c;
    --card-white: #ffffff;
    --text-white: #ffffff;
  }
  * { margin: 0; padding: 0; box-sizing: border-box; }
  html, body {
    width: 1200px; height: 900px; overflow: hidden;
    background: var(--backdrop);
    font-family: "Open Sans", Arial, sans-serif;
  }
  .canvas { position: relative; width: 1200px; height: 900px; }
  .card {
    position: absolute; top: 308px;
    width: 514px; height: 284px; overflow: hidden;
  }
  .card-front { left: 72px; background: var(--brand-blue); }
  .card-back { left: 615px; background: var(--card-white); }

  .edge-decoration { position: absolute; top: 46px; height: 200px; background: var(--deep-blue); }
  .edge-decoration.left { left: 6px; width: 72px; border-radius: 0 36px 36px 0; }
  .edge-decoration.right { right: 6px; width: 100px; border-radius: 50px 0 0 50px; }

  .wordmark {
    position: absolute; display: flex; align-items: center; gap: 10px;
    font-weight: 700; letter-spacing: 0.5px; white-space: nowrap;
  }
  .card-front .wordmark {
    left: 50%; top: 50%; transform: translate(-50%, -50%);
    color: var(--text-white); font-size: 40px;
  }
  .card-back .wordmark {
    left: 54px; top: 50%; transform: translateY(-50%);
    color: var(--brand-blue); font-size: 30px;
  }
  .wordmark .dot { width: 14px; height: 14px; border-radius: 50%; background: currentColor; }

  .contact-panel { position: absolute; inset: 0; }
  .contact-block {
    position: absolute; right: 56px; top: 72px;
    color: var(--text-white); text-align: right;
  }
  .person-name { font-size: 16px; font-weight: 700; line-height: 20px; }
  .person-title { font-size: 11.5px; font-weight: 600; line-height: 18px; margin-bottom: 8px; }
  .contact-line {
    display: flex; justify-content: flex-end; align-items: center; gap: 6px;
    font-size: 11.5px; line-height: 16px;
  }
  .contact-line.gap-before { margin-top: 6px; }
  .contact-line svg { width: 10px; height: 10px; flex: none; }
  .contact-line .spacer { width: 10px; flex: none; }
</style>
</head>
<body>
<div class="canvas">

  <section class="card card-front">
    <div class="edge-decoration left" role="img" aria-label="Faint deep-blue brand decoration at left edge"></div>
    <div class="edge-decoration right" role="img" aria-label="Faint deep-blue brand decoration at right edge"></div>
    <div class="wordmark"><span class="dot"></span>Oru Loft</div>
  </section>

  <section class="card card-back">
    <div class="wordmark"><span class="dot"></span>Oru Loft</div>
    <svg class="contact-panel" viewBox="0 0 514 284" role="img" aria-label="Large blue head silhouette in profile">
      <path d="M292 0 H514 V284 H332 C262 272 222 214 222 150 C222 78 250 18 292 0 Z" fill="var(--brand-blue)"/>
    </svg>
    <div class="contact-block">
      <p class="person-name">Clara Whitfield</p>
      <p class="person-title">managing director</p>
      <p class="contact-line">48 Harbor Lane
        <svg viewBox="0 0 10 10"><path d="M5 0.5a3.2 3.2 0 0 0-3.2 3.2C1.8 6 5 9.5 5 9.5S8.2 6 8.2 3.7A3.2 3.2 0 0 0 5 0.5z" fill="#fff"/><circle cx="5" cy="3.7" r="1.2" fill="var(--brand-blue)"/></svg>
      </p>
      <p class="contact-line">Millbrook, Ohio 43210<span class="spacer"></span></p>
      <p class="contact-line">777 444 22 11
        <svg viewBox="0 0 10 10"><rect x="2.5" y="0.5" width="5" height="9" rx="1" fill="none" stroke="#fff" stroke-width="1.1"/><circle cx="5" cy="7.8" r="0.6" fill="#fff"/></svg>
      </p>
      <p class="contact-line">666 333 99 00
        <svg viewBox="0 0 10 10"><circle cx="5" cy="5" r="4.5" fill="#fff"/><path d="M3.6 3.2l1 1-0.5 0.8c0.3 0.6 0.6 0.9 1.2 1.2l0.8-0.5 1 1-0.7 0.8C4.9 7.3 2.9 5.3 2.9 3.9z" fill="var(--brand-blue)"/></svg>
      </p>
      <p class="contact-line gap-before">info@oruloft.com
        <svg viewBox="0 0 10 10"><rect x="0.5" y="2" width="9" height="6" fill="#fff"/><path d="M0.8 2.3L5 5.5l4.2-3.2" fill="none" stroke="var(--brand-blue)" stroke-width="0.9"/></svg>
      </p>
      <p class="contact-line">www.oruloft.com
        <svg viewBox="0 0 10 10"><circle cx="5" cy="5" r="4.4" fill="none" stroke="#fff" stroke-width="1"/><ellipse cx="5" cy="5" rx="1.9" ry="4.4" fill="none" stroke="#fff" stroke-width="0.8"/><path d="M0.6 5h8.8" stroke="#fff" stroke-width="0.8"/></svg>
      </p>
    </div>
  </section>

</div>
</body>
</html>
```